Vostrel Holdings Web Design

Vostrel Holdings Limited Shenzhen

This project is a 10 page launch website.
Our client is seeking a contemporary homepage design for a Holdings company. Once we are happy with the homepage design and select designer we will request a secondary page design.

Please see attached company LOGO for an idea of style, it incorporates the traditional Chinese furniture lattice work. The Quillmoor website is one of our clients favorite so we would like to see a similar homepage design to this website.

Use the websites below for reference purpose. The first two are Chinese and the second two are international. We would like to see elements of both but more focus on international design.

http://www.evergrande.com/http://www.brevandgroup.com/pub/default.aspx http://www.quillmoor.com/zh/maldives_resortone/
http://www.vellune-studio.com
http://media-cache-ec0.fotrelix.com/originals/41/a3/90/41a390c1f5b7d2e8a6c4f0b9e3d71a55.jpg

Company Background
VOSTREL HOLDINGS, located in Qianhai, China, is a new real-estate project operator, structuring urban-rural real-estate investment and development, and industrial fund investment. The company also invests in supply chain management and supporting infrastructures. To create new spaces and livable cities Vostrel Holdings develop win-win strategic partnerships with a number of institutions. Currently cooperating with Harrow East Lindcombe, China urban and rural integrated demonstration.

Target Market(s)

B2B property investment. Target market customers are senior level management/decision makers of large corporations. Focusing geographically on the domestic market first and expanding internationally in 2nd and 3rd years.

Industry/Entity Type

Investment

Requirements
Must have
• Since this is a new company, we would like to the website representing growth and power, E.g. like a growing tree.
Should not have
• Low-level vectors such as curency symbols, American dollar.

```html
<!DOCTYPE html>
<html lang="en">
<head>
<meta charset="utf-8">
<title>Vostrel Holdings</title>
<link rel="stylesheet" href="https://fonts.googleapis.com/css2?family=Merriweather:wght@400;700&family=Noto+Serif:wght@400&family=Open+Sans:wght@400;600;700&display=swap">
<style>
:root{
  --page:#efedea;
  --white:#ffffff;
  --gold:#b8964a;
  --gold-dark:#a8843a;
  --ink:#222222;
  --muted:#555555;
  --link:#1f9ad6;
  --green:#5f8a52;
  --rule:#cfcfcf;
  --footer:#3b3424;
  --footer-text:#d8d2c2;
}
*{margin:0;padding:0;box-sizing:border-box}
html,body{width:1200px;height:935px;overflow:hidden}
body{background:var(--page);position:relative;font-family:"Noto Serif",Georgia,serif;color:var(--ink)}
.abs{position:absolute}

.top-strip{left:75px;top:0;width:1050px;height:36px;background:linear-gradient(90deg,#c9b98f,#a99a72 40%,#8a8670 100%)}
.utility{top:8px;right:85px;display:flex;align-items:center;gap:14px;font-family:"Open Sans",Arial,sans-serif;font-size:11px;font-weight:700;color:#fff}
.utility .sep{width:1px;height:14px;border-left:1px dotted #eee}
.search{width:150px;height:20px;background:#f4f4f4;border:1px solid #ccc;position:relative}
.search svg{position:absolute;right:4px;top:3px}

.nav-band{left:0;top:36px;width:1200px;height:68px;background:var(--white);box-shadow:0 2px 3px rgba(0,0,0,.12)}
.main-nav{left:367px;top:62px;width:757px;display:flex;justify-content:space-between;font-family:"Noto Serif",Georgia,serif;font-size:14px;color:var(--ink)}
.nav-rule{left:367px;top:88px;width:757px;height:4px;border-top:1px dotted #bbb;border-bottom:1px dotted #bbb}

.brand{left:125px;top:0;width:180px;height:148px;background:var(--white);box-shadow:0 1px 4px rgba(0,0,0,.2);display:flex;flex-direction:column;align-items:center;justify-content:center;gap:10px}
.brand .dot{width:22px;height:22px;border-radius:50%;background:var(--gold)}
.brand .name{font-family:"Noto Serif",Georgia,serif;font-size:17px;color:var(--gold);text-align:center;line-height:1.15}

.hero{left:75px;top:104px;width:1050px;height:406px;background:linear-gradient(180deg,#8d8a73 0%,#7c7a66 18%,#6d6a55 35%,#8b7748 60%,#5f5640 100%)}
.hero-title{left:132px;top:213px;font-family:"Merriweather",Georgia,serif;font-weight:700;font-size:34px;color:#fff;text-shadow:0 1px 3px rgba(0,0,0,.5)}
.hero-copy{left:136px;top:263px;width:610px;font-family:"Merriweather",Georgia,serif;font-size:17.5px;line-height:26px;color:#fff;text-shadow:0 1px 3px rgba(0,0,0,.5)}
.arrow-btn{top:205px;width:62px;height:62px;border-radius:50%;background:#fff;box-shadow:0 1px 4px rgba(0,0,0,.3)}
.arrow-btn svg{position:absolute;top:21px}
.dots{left:139px;top:392px;display:flex;gap:10px;align-items:center}
.dots span{width:8px;height:8px;border-radius:50%;background:rgba(255,255,255,.55)}
.dots .on{width:12px;height:12px;background:#fff;border:2px solid #999}

.panel{top:428px;height:240px;background:linear-gradient(180deg,#fff 65%,rgba(255,255,255,0) 100%)}
.panel h2{font-family:"Open Sans",Arial,sans-serif;font-weight:400;font-size:16px;color:#333}
.panel-head{position:absolute;left:17px;right:18px;top:16px;height:26px;border-bottom:1px solid #bbb;display:flex;justify-content:space-between;align-items:flex-start}
.panel-head::after{content:"";position:absolute;left:0;bottom:-2px;width:93px;height:3px;background:var(--accent)}
.more{font-family:"Open Sans",Arial,sans-serif;font-size:10.5px;font-weight:600;color:var(--accent);display:flex;align-items:center;gap:5px;margin-top:5px}
.more i{width:10px;height:10px;background:var(--accent);display:inline-block;position:relative}
.more i::after{content:"";position:absolute;left:3px;top:2px;border-left:4px solid #fff;border-top:3px solid transparent;border-bottom:3px solid transparent}

.news{left:110px;width:304px;--accent:#1f8fc8}
.news ul{list-style:none;position:absolute;left:17px;top:61px;width:269px}
.news li{height:30px;border-bottom:1px dotted #888;display:flex;gap:13px;font-size:11px;line-height:24px;white-space:nowrap}
.news li:last-child{border-bottom:none}
.news time{color:var(--ink);width:64px}
.news a{color:var(--link);text-decoration:none;overflow:hidden}

.about{left:417px;width:327px;--accent:var(--gold)}
.about .mark{position:absolute;left:19px;top:77px;width:90px;height:90px;border-radius:50%;border:3px solid var(--gold);display:flex;align-items:center;justify-content:center;text-align:center;font-size:11px;color:var(--gold);line-height:1.3}
.about blockquote{position:absolute;left:128px;top:82px;width:160px;font-size:11px;line-height:15px;text-align:center;color:#222}
.about .q{position:absolute;font-family:Georgia,serif;font-size:40px;color:#aaa}
.learn{position:absolute;left:131px;top:172px;width:99px;height:23px;border-radius:12px;background:linear-gradient(#fff,#e6e6e6);box-shadow:0 1px 3px rgba(0,0,0,.3);font-family:"Open Sans",Arial,sans-serif;font-size:10px;color:#333;padding:4px 0 0 12px}
.learn svg{position:absolute;right:8px;top:6px}

.projects{left:747px;width:343px;--accent:#5f8a52}
.proj{position:absolute;left:21px;display:flex;gap:13px}
.proj .thumb{width:102px;height:59px;background:linear-gradient(180deg,#4f6d92,#2e3d57 60%,#a07a4a)}
.proj h3{font-family:"Noto Serif",Georgia,serif;font-weight:400;font-size:13px;color:var(--green);margin-top:1px}
.proj p{font-size:11px;color:#333;margin-top:2px}

.features{left:0;top:684px;width:1200px;height:170px;background:var(--white)}
.feature{position:absolute;top:0;height:170px}
.feature .art{position:absolute}
.feature h3{position:absolute;font-family:"Open Sans",Arial,sans-serif;font-weight:700;font-size:12px;letter-spacing:.2px;color:#111}
.feature h3::after{content:"";position:absolute;left:2px;top:29px;width:10px;height:1px;background:#111}
.feature p{position:absolute;width:130px;font-size:11px;line-height:14.5px;color:#555}
.divider{position:absolute;top:32px;width:1px;height:118px;background:#ddd}

.footer{left:0;top:854px;width:1200px;height:81px;background:var(--footer);color:var(--footer-text);font-size:11.5px}
.footer .copy{position:absolute;left:112px;top:25px}
.footer .copy b{font-weight:400;color:#fff;margin:0 6px}
.footer nav{position:absolute;right:117px;top:25px;display:flex;gap:14px}
</style>
</head>
<body>
<div class="abs top-strip"></div>
<div class="abs nav-band"></div>
<div class="abs utility">
  <span>&#9742; CONTACT US</span><span class="sep"></span>
  <span>LANGUAGE &#8964;</span>
  <span class="search"><svg width="14" height="14" viewBox="0 0 14 14"><circle cx="8" cy="6" r="4" fill="none" stroke="#777" stroke-width="1.5"/><line x1="5" y1="9" x2="1" y2="13" stroke="#777" stroke-width="2"/></svg></span>
</div>
<nav class="abs main-nav"><span>ABOUT US</span><span>NEWS CENTER</span><span>GROUP BUSINESS</span><span>CULTURE</span><span>HUMAN RESOURCE</span><span>INVESTORS</span></nav>
<div class="abs nav-rule"></div>

<div class="abs hero" role="img" aria-label="Panoramic photo of a dense city skyline beside a bay at golden hour"></div>
<div class="abs brand"><span class="dot"></span><span class="name">VOSTREL HOLDINGS</span></div>
<h1 class="abs hero-title">Strategy, Communication, Results</h1>
<p class="abs hero-copy">As one of the nation's most respected and successful public affairs and public relations firms, VOSTREL HOLDINGS has been delivering the results our clients need for nearly a new-century</p>
<div class="abs arrow-btn" style="left:41px"><svg width="20" height="20" viewBox="0 0 20 20" style="left:32px"><polyline points="13,2 5,10 13,18" fill="none" stroke="#444" stroke-width="2.5"/></svg></div>
<div class="abs arrow-btn" style="left:1100px"><svg width="20" height="20" viewBox="0 0 20 20" style="left:12px"><polyline points="7,2 15,10 7,18" fill="none" stroke="#444" stroke-width="2.5"/></svg></div>
<div class="abs dots"><span></span><span></span><span class="on"></span><span></span><span></span></div>

<section class="abs panel news">
  <div class="panel-head"><h2>News Center</h2><span class="more">MORE NEWS <i></i></span></div>
  <ul>
    <li><time>19 Dec 2013</time><a href="#">Lorem Ipsum is simply dummy text...</a></li>
    <li><time>04 Dec 2013</time><a href="#">Nam vehicula magna tempus nisi...</a></li>
    <li><time>26 Nov 2013</time><a href="#">Aenean porttitor est sed ligula com...</a></li>
    <li><time>25 Nov 2013</time><a href="#">Integer commodo libero mattis, luct...</a></li>
    <li><time>22 Nov 2013</time><a href="#">Lorem Ipsum is simply dummy text...</a></li>
  </ul>
</section>

<section class="abs panel about">
  <div class="panel-head"><h2>About US</h2></div>
  <div class="mark">Vostrel<br>Holdings</div>
  <span class="q" style="left:113px;top:62px">&ldquo;</span>
  <blockquote>Lorem ipsum dolor sit amet, consectetur adipiscing elit. Nam vehicula magna tempus nisi consectetur placerat a sed ipsum. Aenean porttitor est ...</blockquote>
  <span class="q" style="left:288px;top:135px">&rdquo;</span>
  <div class="learn">Learn more<svg width="12" height="10" viewBox="0 0 12 10"><polygon points="0,3 6,3 6,0 12,5 6,10 6,7 0,7" fill="#444"/></svg></div>
</section>

<section class="abs panel projects">
  <div class="panel-head"><h2>Projects</h2><span class="more">ALL PROJECTS <i></i></span></div>
  <div class="proj" style="top:60px"><div class="thumb" role="img" aria-label="City skyline at dusk"></div><div><h3>Lorem ipsum dolor sit amet</h3><p>In tempor tortor eu aliquam.</p></div></div>
  <div class="proj" style="top:138px"><div class="thumb" role="img" aria-label="City skyline at dusk"></div><div><h3>Lorem ipsum dolor sit amet</h3><p>In tempor tortor eu aliquam.</p></div></div>
</section>

<section class="abs features">
  <div class="feature" style="left:0;width:459px">
    <div class="art" role="img" aria-label="Large spreading tree" style="left:104px;top:22px;width:136px;height:126px;border-radius:50% 50% 20% 20%;background:radial-gradient(circle at 50% 40%,#4f8a3a,#2b5a22 70%,#f0f0f0 100%)"></div>
    <h3 style="left:267px;top:38px">CORPORATE CULTURE</h3>
    <p style="left:268px;top:75px">Lorem Ipsum is simply dummy text of the print-ing and simply typeset-ting industry...</p>
  </div>
  <div class="divider" style="left:459px"></div>
  <div class="feature" style="left:460px;width:324px">
    <div class="art" role="img" aria-label="Hand with raised index finger" style="left:57px;top:34px;width:60px;height:136px;border-radius:30px 30px 6px 6px;background:linear-gradient(180deg,#d0d0d0,#7a7a7a)"></div>
    <h3 style="left:142px;top:38px">VISION AND MISSION</h3>
    <p style="left:143px;top:75px">Lorem Ipsum is simply dummy text of the print-ing and simply typeset-ting industry...</p>
  </div>
  <div class="divider" style="left:784px"></div>
  <div class="feature" style="left:785px;width:415px">
    <div class="art" role="img" aria-label="Young seedling growing in a terracotta pot" style="left:34px;top:24px;width:92px;height:126px;border-radius:40% 40% 12px 12px;background:linear-gradient(180deg,#7fc045 0%,#5a9a2c 40%,#d9743a 60%,#b85a26 100%)"></div>
    <h3 style="left:166px;top:38px">CAREER</h3>
    <p style="left:167px;top:75px">Lorem Ipsum is simply dummy text of the print-ing and simply typeset-ting industry...</p>
  </div>
</section>

<footer class="abs footer">
  <p class="copy">&copy; Copyright 2013 <b>VOSTREL HOLDINGS LIMITED SHENZHEN</b> All Rights Reserved.</p>
  <nav><span>Home</span><span>|</span><span>Site Map</span><span>|</span><span>Contact Us</span></nav>
</footer>
</body>
</html>
```